Bramwell Resources Ltd. - Refreshed business card challenge

A revised, refreshed business card design for my oil and gas company using my existing logo. Feel free to be as creative as you like!

Target Market(s)

bankers, lawyers

Industry/Entity Type

Oil And Gas Exploration

Contact Information for Business Card

See the "Must Haves" section

Font styles to use
Serif
Sans Serif

Colors

Designer to choose colors to be used in the design.

Requirements
Must have
• Existing business logo, name, title, email, phone number, business address
• Neil Hadley, CA, CPA
• Vice President Finance & Chief Financial Officer
• nhadley@bramwellresources-mail.com
• office: (587)555-0142
• cell: (403)555-0187
• 1400, 815 4 Street S.W.
• Calgary, AB
• T2P 4K8
Should not have
• Should not be plain and boring.

```html
<!DOCTYPE html>
<html lang="en">
<head>
<meta charset="utf-8">
<title>Bramwell Resources Ltd. – Business Card</title>
<link href="https://fonts.googleapis.com/css2?family=Fira+Sans:wght@400;600&display=swap" rel="stylesheet">
<style>
  :root {
    --forest: #0b4a2f;
    --forest-deep: #083a25;
    --steel: #7a7a7a;
    --card: #ffffff;
    --ink: #1f1f1f;
    --backdrop: #d9d9d8;
  }
  * { box-sizing: border-box; margin: 0; padding: 0; }
  html, body { width: 1200px; height: 1045px; overflow: hidden; }
  body {
    background: var(--backdrop);
    font-family: "Fira Sans", Arial, sans-serif;
    color: var(--ink);
    display: flex;
    flex-direction: column;
    align-items: center;
    justify-content: center;
    gap: 45px;
  }
  .card {
    position: relative;
    width: 700px;
    height: 400px;
    background: var(--card);
    overflow: hidden;
    box-shadow: 0 6px 18px rgba(0,0,0,.18);
  }
  .decor {
    position: absolute;
    background: linear-gradient(135deg, var(--forest) 0%, var(--forest-deep) 70%, var(--steel) 100%);
  }
  .decor-front-corner { left: 0; bottom: 0; width: 230px; height: 150px; }
  .decor-front-top { right: 0; top: 0; width: 150px; height: 90px; }
  .decor-back-panel { left: 0; top: 0; width: 260px; height: 400px; }
  .brand {
    position: absolute;
    left: 50%;
    top: 50%;
    transform: translate(-50%, -50%);
    display: flex;
    align-items: center;
    gap: 12px;
    white-space: nowrap;
  }
  .brand-dot {
    width: 18px; height: 18px; border-radius: 50%;
    background: var(--forest);
  }
  .brand-name {
    font-size: 40px;
    font-weight: 600;
    color: var(--forest);
  }
  .contact {
    position: absolute;
    left: 330px;
    top: 60px;
    font-size: 17px;
    line-height: 1.35;
  }
  .contact-name {
    display: flex; align-items: center; gap: 10px;
    font-size: 25px;
    margin-bottom: 4px;
  }
  .contact-title { padding-left: 28px; margin-bottom: 22px; }
  .contact-list { list-style: none; }
  .contact-list li {
    display: flex; align-items: flex-start; gap: 12px;
    margin-bottom: 4px;
  }
  .icon { width: 16px; height: 16px; flex: none; margin-top: 3px; fill: var(--forest); }
</style>
</head>
<body>

<section class="card card-front" aria-label="Card front">
  <div class="decor decor-front-top" role="img" aria-label="Green and steel corner swoosh decoration"></div>
  <div class="decor decor-front-corner" role="img" aria-label="Green and steel wave decoration"></div>
  <div class="brand">
    <span class="brand-dot"></span>
    <span class="brand-name">Bramwell Resources</span>
  </div>
</section>

<section class="card card-back" aria-label="Card back">
  <div class="decor decor-back-panel" role="img" aria-label="Metallic drop emblem on green field"></div>

  <div class="contact">
    <p class="contact-name">
      <svg class="icon" viewBox="0 0 16 16"><circle cx="8" cy="8" r="7"/><circle cx="8" cy="8" r="3" fill="#fff"/></svg>
      Neil Hadley, CA, CPA
    </p>
    <p class="contact-title">Vice President Finance &amp;<br>Chief Financial Officer</p>
    <ul class="contact-list">
      <li>
        <svg class="icon" viewBox="0 0 16 16"><path d="M1 3h14v10H1z M2.5 4.5 8 9l5.5-4.5v7h-11z" fill-rule="evenodd"/></svg>
        nhadley@bramwellresources-mail.com
      </li>
      <li>
        <svg class="icon" viewBox="0 0 16 16"><path d="M4 1l3 3-1.6 2a9 9 0 0 0 4.6 4.6L12 9l3 3-2 3C7 14 2 9 1 3z"/></svg>
        (587)555-0142
      </li>
      <li>
        <svg class="icon" viewBox="0 0 16 16"><path d="M4 1h8v14H4z M5.5 2.5v9h5v-9z" fill-rule="evenodd"/></svg>
        (403)555-0187
      </li>
      <li>
        <svg class="icon" viewBox="0 0 16 16"><path d="M8 1a5 5 0 0 1 5 5c0 4-5 9-5 9S3 10 3 6a5 5 0 0 1 5-5z M8 4a2 2 0 1 0 0 4 2 2 0 0 0 0-4z" fill-rule="evenodd"/></svg>
        <span>1400, 815 4 Street S.W.<br>Calgary, AB<br>T2P 4K8</span>
      </li>
    </ul>
  </div>
</section>

</body>
</html>
```